Public Assistance Direct mail piece

need a full color 2 sided marketing brochure to use in direct mail campaign. finished product will be printed on 2 times. initially full color brochures to be printed in bulk. Then consumer contact info and case manager contact info will be added at a later date.
brochure will need to have 2 blank areas on front side to print address that will show thru window envelope and sales agent info on for mail campaign.
Would like to see designs that include our current color scheme and logo.
Target market. Low income poverty. Non profit service offering free assistance to help low income seniors get free assitance thru state and federal public assistance programs.
1. Tovalink - over 1 in 5 recieve help from state Tovalink. Tovalink programs for seniors and persons on Sunbrook can pay doctor copays, deductibles, and assist with medical bills.
2. Brightway Program - receive Federal assistance with prescription medications, deductibles, copays, and drug plan premiums.
3. Sunbrook Savings Program - many adults 65 and over are eligible to receive Sunbrook at no cost. The program will pay your Sunbrook Part B premium and can even refund some previous payments.

You may be eligible to participate in one or more of these programs. All programs are based on limited income and assets.

To learn more call your local county case manager.

Knowledge is Power. Lets up help empower you.
Pay it forward. Who else do you know that is on Sunbrook that could use some help?

many graphs and illustrations are available form each government agency.

Target Market(s)

Seniors 65 plus, Sunbrook recipients

Industry/Entity Type

Marketing

Colors
0355a3
ec1f27
ffffff

Requirements
Must have
• logo, non profit, will need a government disclaimer somewhere
Nice to have
• photos of seniors saving money.

```html
<!DOCTYPE html>
<html lang="en">
<head>
<meta charset="utf-8">
<title>Elderwell Aid Center – Direct Mail Brochure</title>
<link rel="stylesheet" href="https://fonts.googleapis.com/css2?family=Montserrat:wght@300;400;500;700;800&display=swap">
<style>
  :root{
    --navy:#1b2f5e;
    --blue:#0355a3;
    --red:#ec1f27;
    --white:#ffffff;
    --paper:#f4f4f5;
    --card:#e9eaec;
    --ink:#2a2a2a;
    --grey:#9a9ca1;
    --line:#d9dadd;
    --stage:#e6e7e9;
  }
  *{box-sizing:border-box;margin:0;padding:0}
  html,body{width:1200px;height:784px;overflow:hidden;background:var(--stage);font-family:"Montserrat",Arial,sans-serif;color:var(--ink)}
  .canvas{position:relative;width:1200px;height:784px}
  .page{position:absolute;top:44px;width:532px;height:696px;background:var(--paper);overflow:hidden;box-shadow:0 6px 18px rgba(0,0,0,.18)}
  .page--front{left:46px}
  .page--back{left:622px}
  .abs{position:absolute}

  /* brand */
  .brand{display:flex;align-items:center;gap:10px}
  .brand__dot{width:34px;height:34px;border-radius:50%;background:var(--red);flex:none}
  .brand__name{font-weight:700;color:var(--navy);font-size:22px;line-height:1.05;text-transform:uppercase;letter-spacing:.5px}
  .brand__tag{font-size:9px;letter-spacing:.5px;color:var(--navy);text-transform:uppercase;margin-top:6px;white-space:nowrap}

  /* front */
  .front__brand{top:34px;left:270px}
  .hero__lead{top:372px;left:30px;font-size:28px;font-weight:300;color:var(--red)}
  .hero__title{top:404px;left:30px;font-size:28px;font-weight:800;color:var(--navy);letter-spacing:-.3px}
  .hero__sub{top:436px;left:30px;font-size:28px;font-weight:300;color:var(--ink)}
  .hero__rule{top:476px;left:30px;width:62px;height:2px;background:var(--navy)}
  .intro{top:486px;left:30px;width:474px;font-size:7.6px;line-height:1.65;color:#333}
  .mail-box{top:566px;height:72px;border:1px solid var(--line);border-radius:6px;background:#eeeff0;display:flex;align-items:center;justify-content:center;font-size:8px;letter-spacing:3px;color:#a7a9ad;text-transform:uppercase}
  .mail-box--address{left:30px;width:218px}
  .mail-box--agent{left:277px;width:219px}

  /* footer band */
  .contact-bar{left:0;bottom:0;width:532px;height:42px}
  .contact-bar__phone{position:absolute;left:26px;top:6px;display:flex;align-items:center;gap:8px;color:var(--white);font-weight:800;font-size:26px;letter-spacing:.3px}
  .contact-bar__toll{font-size:7px;font-weight:500;line-height:1;letter-spacing:.5px}
  .contact-bar__web{position:absolute;right:18px;top:14px;display:flex;align-items:center;gap:6px;color:var(--white);font-weight:700;font-size:11px}

  /* back */
  .back__headline{top:96px;left:29px;font-size:38px;line-height:1.12;font-weight:800;color:var(--red);letter-spacing:-.5px}
  .back__headline .is{font-weight:300;color:var(--red)}
  .back__headline .power{color:var(--navy)}
  .back__tagline{top:182px;left:29px;font-size:18px;font-weight:400;color:var(--red)}
  .back__referral{top:218px;left:29px;width:280px;font-size:18px;line-height:1.3;font-weight:300;color:var(--ink)}

  .program{top:364px;width:150px;height:148px;background:var(--card);border-radius:4px;text-align:center;padding:8px 10px 0}
  .program--tovalink{left:30px}
  .program--brightway{left:191px}
  .program--savings{left:352px}
  .program__name{font-size:14px;font-weight:800;color:var(--navy);line-height:1.12}
  .program__name em{display:block;font-style:normal;color:var(--red);font-size:12.5px}
  .program__name--small{font-size:13.5px}
  .program__text{margin-top:8px;font-size:7.9px;line-height:1.5;color:#333;text-align:justify;text-align-last:center;hyphens:auto}
  .program--tovalink .program__text{margin-top:12px}
  .icon{top:312px;width:46px;height:46px}
  .icon--tovalink{left:82px}
  .icon--brightway{left:243px}
  .icon--savings{left:404px}

  .back__brand{top:528px;left:0;width:532px;display:flex;flex-direction:column;align-items:center}
  .back__cta{top:636px;left:0;width:532px;text-align:center;font-size:13px;font-weight:400;color:var(--navy)}
  .back__cta strong{color:var(--red);font-weight:800}
</style>
</head>
<body>
<main class="canvas">

  <!-- FRONT -->
  <section class="page page--front" aria-label="Brochure front">
    <svg class="abs" width="532" height="696" viewBox="0 0 532 696" aria-hidden="true" style="left:0;top:0">
      <path d="M0,282 C140,350 300,380 532,250 L532,290 C300,420 150,380 0,310 Z" fill="var(--navy)"/>
      <path d="M0,306 C150,376 300,414 532,286 L532,292 C300,422 150,384 0,312 Z" fill="var(--red)"/>
      <path d="M360,300 C420,282 480,260 532,232 L532,250 C480,280 430,300 372,318 Z" fill="var(--red)"/>
    </svg>
    <svg class="abs" width="532" height="360" viewBox="0 0 532 360" role="img" aria-label="Photo of a senior couple saving coins in a piggy bank at home" style="left:0;top:0">
      <defs><linearGradient id="frontPhoto" x1="0" y1="0" x2="1" y2="1"><stop offset="0" stop-color="#e9e3dc"/><stop offset="1" stop-color="#b9a58f"/></linearGradient></defs>
      <path d="M0,0 H210 C220,120 300,220 532,230 L532,250 C300,380 140,350 0,282 Z" fill="url(#frontPhoto)"/>
    </svg>
    <svg class="abs" width="210" height="210" viewBox="0 0 210 210" role="img" aria-label="Photo of a smiling senior couple outdoors" style="left:302px;top:230px">
      <defs><linearGradient id="circleFront" x1="0" y1="0" x2="0" y2="1"><stop offset="0" stop-color="#9cc3e0"/><stop offset="1" stop-color="#c89a7a"/></linearGradient></defs>
      <circle cx="105" cy="105" r="103" fill="#dcdde0"/>
      <circle cx="105" cy="105" r="95" fill="url(#circleFront)"/>
    </svg>

    <div class="abs front__brand brand">
      <span class="brand__dot"></span>
      <div>
        <div class="brand__name">Elderwell<br>Aid Center</div>
        <div class="brand__tag">Life, Health and Wealth Protection</div>
      </div>
    </div>

    <h1 class="abs hero__lead">We Create</h1>
    <h2 class="abs hero__title">SUCCESS STORIES</h2>
    <p class="abs hero__sub">one family at a time</p>
    <div class="abs hero__rule"></div>
    <p class="abs intro">Our goal is simple. To create success stories, one family at a time. There are hundreds of insurance companies in the US today, all with multiple programs available. With so many options available how are you supposed to find the right one for you? You could shop forever and never find the right programs or thebest rates. What everyone sees's thru the media is the best advertisement and marketing, not which programs actually fit them. Every day we get asked questions, such as.</p>

    <div class="abs mail-box mail-box--address">Address goes here</div>
    <div class="abs mail-box mail-box--agent">Sales agent info</div>

    <footer class="abs contact-bar">
      <svg class="abs" width="532" height="42" viewBox="0 0 532 42" aria-hidden="true" style="left:0;top:0">
        <path d="M0,0 H312 L292,42 H0 Z" fill="var(--navy)"/>
        <path d="M318,0 H532 V42 H298 Z" fill="var(--red)"/>
      </svg>
      <div class="contact-bar__phone">
        <svg width="18" height="18" viewBox="0 0 24 24" aria-hidden="true"><circle cx="12" cy="12" r="12" fill="var(--red)"/><path d="M8 6c1 0 1.5 2 2 3s-1 1.5-.8 2.2c.5 1.3 1.8 2.6 3.1 3.1.7.2 1.2-1.3 2.2-.8s3 1 3 2-1 2.5-2.5 2.5C10 18 6 14 6 8.5 6 7 7 6 8 6z" fill="var(--white)"/></svg>
        877-555-0142
        <span class="contact-bar__toll">TOLL<br>FREE</span>
      </div>
      <div class="contact-bar__web">
        <svg width="11" height="11" viewBox="0 0 24 24" aria-hidden="true"><circle cx="12" cy="12" r="10" fill="none" stroke="var(--white)" stroke-width="2"/><path d="M2 12h20M12 2c3 3 3 17 0 20M12 2c-3 3-3 17 0 20" fill="none" stroke="var(--white)" stroke-width="1.6"/></svg>
        WWW.ELDERWELLAID.ORG
      </div>
    </footer>
  </section>

  <!-- BACK -->
  <section class="page page--back" aria-label="Brochure back">
    <svg class="abs" width="532" height="120" viewBox="0 0 532 120" aria-hidden="true" style="left:0;top:0">
      <path d="M0,0 H532 V6 C420,40 330,60 230,52 C140,46 60,30 0,24 Z" fill="var(--navy)"/>
      <path d="M36,0 H360 C300,30 250,40 200,36 C140,30 90,12 36,0 Z" fill="var(--red)"/>
      <path d="M230,52 C330,60 420,40 532,6 V14 C420,52 320,70 230,58 Z" fill="#c9cbcf"/>
    </svg>
    <svg class="abs" width="252" height="252" viewBox="0 0 252 252" role="img" aria-label="Photo of a senior man meeting with a case manager at a table" style="left:290px;top:24px">
      <defs><linearGradient id="circleBack" x1="0" y1="0" x2="1" y2="1"><stop offset="0" stop-color="#e9e4da"/><stop offset="1" stop-color="#8f7a66"/></linearGradient></defs>
      <circle cx="126" cy="126" r="124" fill="#dcdde0"/>
      <circle cx="126" cy="126" r="116" fill="url(#circleBack)"/>
    </svg>

    <h2 class="abs back__headline">KNOWLEDGE<br><span class="is">IS</span> <span class="power">POWER</span></h2>
    <p class="abs back__tagline">Lets up help empower you</p>
    <p class="abs back__referral">Pay it forward. Who else do you know that is on Sunbrook that could use some help?</p>

    <svg class="abs icon icon--tovalink" viewBox="0 0 48 48" aria-hidden="true">
      <circle cx="24" cy="24" r="23" fill="var(--white)" stroke="var(--red)" stroke-width="1.5"/>
      <circle cx="24" cy="24" r="19" fill="var(--red)"/>
      <path d="M17 14v7a5 5 0 0 0 10 0v-7M22 26v4a5 5 0 0 0 10 0v-3" fill="none" stroke="var(--white)" stroke-width="1.8" stroke-linecap="round"/>
      <circle cx="32" cy="25" r="2.2" fill="none" stroke="var(--white)" stroke-width="1.6"/>
    </svg>
    <svg class="abs icon icon--brightway" viewBox="0 0 48 48" aria-hidden="true">
      <circle cx="24" cy="24" r="23" fill="var(--white)" stroke="var(--red)" stroke-width="1.5"/>
      <circle cx="24" cy="24" r="19" fill="var(--red)"/>
      <g transform="rotate(-45 24 24)"><rect x="13" y="19" width="22" height="10" rx="5" fill="var(--white)"/></g>
      <path d="M24 24 l4.2 -4.2" stroke="var(--red)" stroke-width="1.6"/>
    </svg>
    <svg class="abs icon icon--savings" viewBox="0 0 48 48" aria-hidden="true">
      <circle cx="24" cy="24" r="23" fill="var(--white)" stroke="var(--red)" stroke-width="1.5"/>
      <circle cx="24" cy="24" r="19" fill="var(--red)"/>
      <path d="M33 20a10 10 0 1 0 1 6" fill="none" stroke="var(--white)" stroke-width="1.8" stroke-linecap="round"/>
      <path d="M34 15v6h-6" fill="none" stroke="var(--white)" stroke-width="1.8" stroke-linecap="round"/>
      <text x="24" y="28.5" text-anchor="middle" font-family="Montserrat, sans-serif" font-weight="700" font-size="12" fill="var(--white)">$</text>
    </svg>

    <article class="abs program program--tovalink">
      <h3 class="program__name" style="margin-top:6px">TOVALINK</h3>
      <p class="program__text">over 1 in 5 recieve help from state Tovalink. Tovalink programs for seniors and persons on Sunbrook can pay doctor copays, deductibles, and assist with medical bills.</p>
    </article>
    <article class="abs program program--brightway">
      <h3 class="program__name" style="margin-top:6px">BRIGHTWAY<em>PROGRAM</em></h3>
      <p class="program__text">receive Federal assistance with prescription medications, deductibles, copays, and drug plan premiums.</p>
    </article>
    <article class="abs program program--savings">
      <h3 class="program__name program__name--small" style="margin-top:6px">SUNBROOK<em>SAVINGS PROGRAM</em></h3>
      <p class="program__text">many adults 65 and over are eligible to receive Sunbrook at no cost. The program will pay your Sunbrook Part B premium and can even refund some previous payments.</p>
    </article>

    <div class="abs back__brand">
      <div class="brand">
        <span class="brand__dot"></span>
        <div class="brand__name">Elderwell<br>Aid Center</div>
      </div>
      <div class="brand__tag">Life, Health and Wealth Protection</div>
    </div>

    <p class="abs back__cta">TO LEARN MORE <strong>CALL YOUR LOCAL COUNTY</strong> CASE MANAGER</p>

    <footer class="abs contact-bar">
      <svg class="abs" width="532" height="42" viewBox="0 0 532 42" aria-hidden="true" style="left:0;top:0">
        <path d="M0,0 H312 L292,42 H0 Z" fill="var(--navy)"/>
        <path d="M318,0 H532 V42 H298 Z" fill="var(--red)"/>
      </svg>
      <div class="contact-bar__phone">
        <svg width="18" height="18" viewBox="0 0 24 24" aria-hidden="true"><circle cx="12" cy="12" r="12" fill="var(--red)"/><path d="M8 6c1 0 1.5 2 2 3s-1 1.5-.8 2.2c.5 1.3 1.8 2.6 3.1 3.1.7.2 1.2-1.3 2.2-.8s3 1 3 2-1 2.5-2.5 2.5C10 18 6 14 6 8.5 6 7 7 6 8 6z" fill="var(--white)"/></svg>
        877-555-0142
        <span class="contact-bar__toll">TOLL<br>FREE</span>
      </div>
      <div class="contact-bar__web">
        <svg width="11" height="11" viewBox="0 0 24 24" aria-hidden="true"><circle cx="12" cy="12" r="10" fill="none" stroke="var(--white)" stroke-width="2"/><path d="M2 12h20M12 2c3 3 3 17 0 20M12 2c-3 3-3 17 0 20" fill="none" stroke="var(--white)" stroke-width="1.6"/></svg>
        WWW.ELDERWELLAID.ORG
      </div>
    </footer>
  </section>

</main>
</body>
</html>
```